Business Card, Stationary with Shark Logo for Personal Injury Lawyer

I need business cards and stationery with a shark logo for my Personal Injury Law Practice. Has to have this written on it:
Martin K. Holloway
Injury Lawyer
The Copperfield Building
718 Wexley Street
Millbrook, Harbor State 02990
401-555-0172
Martinholloway.example

Contact Information for Business Card

Martin K. Holloway, Injury Lawyer, address, 401-555-0172, martinholloway.example

```html
<!DOCTYPE html>
<html lang="en">
<head>
<meta charset="utf-8">
<title>Martin K. Holloway – Business Card</title>
<link rel="stylesheet" href="https://fonts.googleapis.com/css2?family=Montserrat:wght@400;500;600;800&display=swap">
<style>
  :root {
    --page-bg: #c6c8ca;
    --card-navy: #2b2766;
    --card-navy-light: #312d70;
    --card-blue: #2f4680;
    --mark-tone: #3a3683;
    --text-white: #ffffff;
    --photo-dark: #2a2f45;
    --photo-mid: #4a5470;
    --photo-light: #8d96ad;
  }
  * { margin: 0; padding: 0; box-sizing: border-box; }
  html, body {
    width: 1200px;
    height: 928px;
    overflow: hidden;
  }
  body {
    background: var(--page-bg);
    font-family: "Montserrat", sans-serif;
    display: flex;
    flex-direction: column;
    align-items: center;
    justify-content: center;
    gap: 42px;
  }
  .card {
    position: relative;
    width: 670px;
    height: 383px;
    border-radius: 16px;
    overflow: hidden;
  }
  .card-front {
    background: radial-gradient(ellipse at 50% 75%, var(--card-navy-light), var(--card-navy) 70%);
    display: flex;
    flex-direction: column;
    align-items: center;
    justify-content: center;
    gap: 10px;
  }
  .front-name {
    color: var(--mark-tone);
    font-weight: 800;
    font-size: 40px;
    letter-spacing: -0.5px;
  }
  .front-title {
    color: var(--mark-tone);
    font-weight: 800;
    font-size: 18px;
    letter-spacing: 9px;
    text-transform: uppercase;
  }
  .card-back {
    background: linear-gradient(90deg, var(--card-navy) 0%, var(--card-navy) 25%, var(--card-blue) 62%, var(--card-navy) 100%);
    color: var(--text-white);
  }
  .portrait {
    position: absolute;
    top: 0;
    right: 0;
    width: 380px;
    height: 100%;
    background: linear-gradient(180deg, var(--photo-light) 0%, var(--photo-mid) 45%, var(--photo-dark) 100%);
    -webkit-mask-image: linear-gradient(90deg, transparent 0%, #000 40%);
    mask-image: linear-gradient(90deg, transparent 0%, #000 40%);
  }
  .brand {
    position: absolute;
    left: 42px;
    top: 50px;
  }
  .brand-name {
    font-weight: 800;
    font-size: 32px;
    line-height: 1.08;
    letter-spacing: -0.3px;
  }
  .brand-title {
    margin-top: 10px;
    font-weight: 800;
    font-size: 15px;
    letter-spacing: 7px;
    text-transform: uppercase;
  }
  .contact {
    position: absolute;
    left: 45px;
    top: 202px;
    font-size: 15.5px;
    letter-spacing: 0.7px;
  }
  .contact-line { margin-bottom: 14px; }
  .contact-label { font-weight: 600; }
  .address {
    margin-top: 20px;
    font-size: 15.5px;
    line-height: 1.4;
    letter-spacing: 0.7px;
  }
  .address-building { font-weight: 600; }
</style>
</head>
<body>
  <section class="card card-front">
    <div class="front-name">Martin K. Holloway</div>
    <div class="front-title">Injury Lawyer</div>
  </section>

  <section class="card card-back">
    <div class="portrait" role="img" aria-label="Portrait photo of the lawyer in a suit against a city backdrop"></div>
    <div class="brand">
      <div class="brand-name">Martin K.<br>Holloway</div>
      <div class="brand-title">Injury Lawyer</div>
    </div>
    <div class="contact">
      <p class="contact-line"><span class="contact-label">Call Or Text:</span> 401-555-0172</p>
      <p class="contact-line"><span class="contact-label">Visit:</span> Martinholloway.example</p>
      <div class="address">
        <p class="address-building">The Copperfield Building</p>
        <p>718 Wexley Street</p>
        <p>Millbrook, Harbor State 02990</p>
      </div>
    </div>
  </section>
</body>
</html>
```